Pell Tor Website

Need a website that will highlight our product and provide a storefront for purchases. The design of the site (colors, logo, theme) needs to closely match the design of the product packaging and I am including files and ai file of this packaging.

Target Market(s)

Males and Females aged 16-70.

Number of Pages Required

4 page

Font styles to use
Serif

Requirements
Must have
• Home page, Product Page, Contact us page, Shop Page
• Use the general design theme that is shown in the attached AI file. Must have Pell Tor logo, must have pictures of the bugs as shown in the packaging. Can use all of the information on the ai file.
Nice to have
• Bold, clear, clean.

```html
<!DOCTYPE html>
<html lang="en">
<head>
<meta charset="utf-8">
<title>Pell Tor</title>
<link href="https://fonts.googleapis.com/css2?family=Montserrat:wght@400;600;700;800;900&family=Open+Sans:wght@400;600&display=swap" rel="stylesheet">
<style>
  :root{
    --red:#c4161c;
    --red-dark:#8e0f13;
    --black:#141414;
    --charcoal:#2a2a2a;
    --yellow:#ffe100;
    --white:#ffffff;
    --grey:#666666;
    --light:#f2f2f2;
  }
  *{box-sizing:border-box;margin:0;padding:0}
  html,body{width:786px;height:1200px;overflow:hidden;background:var(--white)}
  body{font-family:"Open Sans",Arial,sans-serif;color:var(--black)}
  .canvas{position:relative;width:786px;height:1200px;overflow:hidden}

  /* header + hero */
  .hero{position:absolute;left:0;top:0;width:786px;height:370px;
    background:radial-gradient(circle at 70% 40%,#d8232a 0%,var(--red) 45%,var(--red-dark) 100%)}
  .brand{position:absolute;left:22px;top:14px;display:flex;align-items:center;gap:6px;
    background:var(--black);padding:6px 10px;border-radius:4px}
  .brand-dot{width:14px;height:14px;background:var(--yellow);border-radius:50%}
  .brand-name{font-family:"Montserrat",sans-serif;font-weight:800;font-size:14px;color:var(--white)}
  .account{position:absolute;right:24px;top:10px;display:flex;gap:10px}
  .pill{font-family:"Montserrat",sans-serif;font-size:8px;font-weight:700;padding:3px 14px;border-radius:10px}
  .pill.login{background:var(--yellow);color:var(--black)}
  .pill.signup{border:1px solid var(--yellow);color:var(--white)}
  .nav{position:absolute;right:24px;top:42px;display:flex;gap:14px;list-style:none}
  .nav li{font-family:"Montserrat",sans-serif;font-size:8.5px;font-weight:700;color:var(--white)}

  .headline{position:absolute;left:45px;top:92px;font-family:"Montserrat",sans-serif;
    font-weight:900;font-size:44px;line-height:44px;color:var(--white);letter-spacing:1px}
  .pack{position:absolute;left:45px;top:190px;font-family:"Montserrat",sans-serif;font-weight:700;
    font-size:15px;line-height:17px;color:var(--white)}
  .features{position:absolute;left:45px;top:228px;list-style:none}
  .features li{font-size:8.5px;line-height:13px;color:var(--white);padding-left:10px;position:relative}
  .features li::before{content:"";position:absolute;left:0;top:5px;width:4px;height:4px;background:var(--yellow);border-radius:50%}
  .order{position:absolute;left:45px;top:296px;background:var(--yellow);color:var(--black);
    font-family:"Montserrat",sans-serif;font-weight:800;font-size:11px;padding:8px 18px;border-radius:16px}
  .boot-art{position:absolute;left:440px;top:58px;width:300px;height:340px;
    background:linear-gradient(160deg,#ffe100 0%,#e0c000 30%,#9a9a9a 55%,#4a4a4a 100%);
    border-radius:150px 150px 24px 24px}

  /* pest band */
  .pests{position:absolute;left:0;top:370px;width:786px;height:52px;background:var(--black);
    display:flex;gap:16px;padding-left:40px;align-items:center}
  .pest{display:flex;flex-direction:column;align-items:center;gap:3px;width:32px}
  .pest-icon{width:22px;height:20px;background:#555;border-radius:4px}
  .pest span{font-size:8px;color:var(--white)}

  /* about */
  .section-title{position:absolute;left:0;width:786px;text-align:center;font-family:"Montserrat",sans-serif;
    font-weight:800;font-size:19px;letter-spacing:1px;color:var(--black)}
  .section-title::before,.section-title::after{content:"";display:inline-block;width:60px;height:2px;
    background:var(--red);vertical-align:middle;margin:0 12px}
  .about-title{top:448px}
  .about-text{position:absolute;left:90px;top:482px;width:606px;font-size:8.5px;line-height:13px;color:var(--grey)}

  /* products */
  .products-title{top:584px}
  .product{position:absolute;top:620px;width:186px;height:200px;background:var(--white);
    box-shadow:0 2px 8px rgba(0,0,0,.15)}
  .product-photo{position:absolute;left:38px;top:14px;width:110px;height:140px;
    background:linear-gradient(180deg,#3a3a3a,#111);border-radius:8px}
  .shop{position:absolute;left:43px;top:166px;width:100px;text-align:center;background:var(--yellow);
    font-family:"Montserrat",sans-serif;font-weight:800;font-size:10px;padding:6px 0;border-radius:14px}
  .view-all{position:absolute;left:316px;top:846px;width:154px;text-align:center;background:var(--red);
    color:var(--white);font-family:"Montserrat",sans-serif;font-weight:700;font-size:9.5px;padding:9px 0;border-radius:18px}

  /* subscribe */
  .subscribe-title{position:absolute;top:920px;left:0;width:786px;text-align:center;font-family:"Montserrat",sans-serif;
    font-weight:600;font-size:20px;color:var(--black)}
  .subscribe-form{position:absolute;left:248px;top:966px;display:flex}
  .subscribe-input{width:200px;height:22px;border:none;border-bottom:1px solid #bbb;font-size:8px;color:#999;padding:5px 4px}
  .subscribe-btn{height:22px;background:var(--red);color:var(--white);font-size:9px;padding:5px 18px}

  /* footer */
  .footer{position:absolute;left:0;top:1030px;width:786px;height:170px;background:var(--black);color:var(--white)}
  .f-col{position:absolute;top:10px}
  .f-col h4{font-family:"Montserrat",sans-serif;font-weight:600;font-size:12px;margin-bottom:6px}
  .f-col p,.f-col li{font-size:7.5px;line-height:11px;color:#ccc;list-style:none}
  .contact{left:95px}
  .links{left:345px}
  .links .cols{display:flex;gap:60px}
  .social{left:560px}
  .social-icons{display:flex;gap:6px}
  .social-icons i{width:16px;height:16px;border:1px solid #ccc;border-radius:50%;display:block}
  .copyright{position:absolute;left:0;bottom:0;width:786px;height:20px;border-top:1px solid #333;
    text-align:center;font-size:7.5px;line-height:20px;color:#aaa}
</style>
</head>
<body>
<div class="canvas">
  <header class="hero">
    <div class="brand"><span class="brand-dot"></span><span class="brand-name">Pell Tor</span></div>
    <div class="account"><span class="pill login">LOGIN</span><span class="pill signup">SIGN UP</span></div>
    <ul class="nav"><li>HOME</li><li>ABOUT US</li><li>PRODUCTS</li><li>CONTACT US</li><li>&#128722;</li></ul>

    <h1 class="headline">WHAT'S IN<br>YOUR BOOT?</h1>
    <p class="pack">PACKAGE CONTAINS<br>ONE PAIR (2pcs)</p>
    <ul class="features">
      <li>Durable poly-blend covers</li>
      <li>Reusable</li>
      <li>One size fits all</li>
      <li>Machine washable</li>
      <li>Secure elastic provides fit</li>
    </ul>
    <span class="order">ORDER NOW</span>
    <div class="boot-art" role="img" aria-label="Illustration of a boot with a yellow cap fitted over its opening, set on a dark circle"></div>
  </header>

  <section class="pests">
    <div class="pest"><div class="pest-icon" role="img" aria-label="Spider icon"></div><span>spider</span></div>
    <div class="pest"><div class="pest-icon" role="img" aria-label="Mouse icon"></div><span>mice</span></div>
    <div class="pest"><div class="pest-icon" role="img" aria-label="Snake icon"></div><span>snakes</span></div>
    <div class="pest"><div class="pest-icon" role="img" aria-label="Wasp icon"></div><span>wasps</span></div>
    <div class="pest"><div class="pest-icon" role="img" aria-label="Bug icon"></div><span>bugs</span></div>
    <div class="pest"><div class="pest-icon" role="img" aria-label="Scorpion icon"></div><span>scorpions</span></div>
  </section>

  <h2 class="section-title about-title">ABOUT PELL TOR</h2>
  <p class="about-text">Lorem Ipsum is simply dummy text of the printing and typesetting industry. Lorem Ipsum has been the industry's standard dummy text ever since the 1500s, when an unknown printer took a galley of type and scrambled it to make a type specimen book. It has survived not only five centuries, but also the leap into electronic typesetting, remaining essentially unchanged. It was popularised in the 1960s with the release of Letraset sheets containing Lorem Ipsum passages, and more recently with desktop.</p>

  <h2 class="section-title products-title">OUR PRODUCTS</h2>
  <article class="product" style="left:90px"><div class="product-photo" role="img" aria-label="Photo of a black boot"></div><span class="shop">SHOP NOW</span></article>
  <article class="product" style="left:300px"><div class="product-photo" role="img" aria-label="Photo of a black boot"></div><span class="shop">SHOP NOW</span></article>
  <article class="product" style="left:510px"><div class="product-photo" role="img" aria-label="Photo of a black boot"></div><span class="shop">SHOP NOW</span></article>
  <span class="view-all">VIEW ALL PRODUCTS</span>

  <h2 class="subscribe-title">Subscribe to news and updates</h2>
  <div class="subscribe-form"><span class="subscribe-input">Enter email address</span><span class="subscribe-btn">Subscribe</span></div>

  <footer class="footer">
    <div class="f-col contact">
      <h4>Contact us</h4>
      <p>Northfield Goods Group LLC</p>
      <p>12 Harbor Lane</p>
      <p>Greenfield, OR 97000</p>
      <p>555-010-4821</p>
      <p>www.pelltor.com</p>
      <p>PATENT PENDING</p>
      <p>Made in China</p>
    </div>
    <div class="f-col links">
      <h4>Useful Links</h4>
      <div class="cols">
        <ul><li>Home</li><li>About us</li><li>Products</li><li>Contact Us</li><li>My Account</li><li>Login</li><li>Sign up</li></ul>
        <ul><li>Help Center</li><li>Warranty</li><li>Shipping</li><li>Returns</li><li>Contact Us</li><li>Support</li></ul>
      </div>
    </div>
    <div class="f-col social">
      <h4>Social Media</h4>
      <div class="social-icons"><i></i><i></i><i></i><i></i></div>
    </div>
    <div class="copyright">&copy; pelltor.com</div>
  </footer>
</div>
</body>
</html>
```